A wordpress website for the coolest Resort App

We have developed a mobile app - Zapply and we want to develop a cool, neat and simple wordpress website for it.

I have attached the basics in a keynote/ ppt - but i need you to bring it more to life. plus there are additions:

FOr the number of pages, we will have:
1- Home: very similar to the one pager
2- How it works: Showing step by step on how the app works, and how it connects to the POS system of the restaurant etc with spanshots from the app
3- Benefit: Elaborating more on each of the benefits that is mentioned in the ONE PAGE document, with additional statistics, reference etc.. and embedded videos and animation
4- who we are page
5- In the press page: links to the articles where zapply was mentioned
6- Get in touch page
7- FAQ
Updates

Project Deadline Extended Reason: The first deadline was set for the 1 page website, now i am extending it for the full wesbite development.Still i need the one pager by the 17th, but for the rest we have more time Added Friday, September 15, 2017

Target Market(s)

Resorts, hotels, beach and pool restaurant operators

Industry/Entity Type

Hospitality

Coding

Coded - Design and coding required

Font styles to use
Other font styles liked:
• I have attached the fonts i want to use: ROboto is the main font

Colors

Designer to choose colors to be used in the design.

Requirements
Must have
• Logo, icons for each benefit, you can also use the mood picture i attached or any other picture you recommend - maybe just something related to the app
• I also attached the Main colour, the orange and the blue is the accent one
• I attached the fonts, roboto is the main one
• there should also be a contact us:
• Email : info@zapplyhub.example
• Mobile: +971 5 23 47 90 12
• Address: Harbor Quarter - Coral Bay - Sunreef Islands

```html
<!DOCTYPE html>
<html lang="en">
<head>
<meta charset="utf-8">
<title>Zapply – Hospitality App</title>
<link href="https://fonts.googleapis.com/css2?family=Roboto:ital,wght@0,300;0,400;0,500;0,700;0,900;1,400;1,500;1,700&display=swap" rel="stylesheet">
<style>
:root{
  --orange:#f26b3a;
  --orange-soft:#f6895c;
  --blue:#3a9bd5;
  --blue-dark:#2a86bf;
  --ink:#2e3338;
  --text:#5b6168;
  --muted:#8a9097;
  --dark:#34393e;
  --line:#e3e6e9;
  --white:#ffffff;
}
*{box-sizing:border-box;margin:0;padding:0}
html,body{width:1200px;height:5187px;overflow:hidden}
body{font-family:"Roboto",sans-serif;color:var(--text);background:var(--white);position:relative}
section,header,footer{position:absolute;left:0;width:1200px;overflow:hidden}
.abs{position:absolute}
.section-title{position:absolute;left:0;width:100%;text-align:center;font-size:40px;font-weight:700;font-style:italic;color:var(--ink)}
.section-title .accent{color:var(--orange)}
.section-lead{position:absolute;left:50%;transform:translateX(-50%);width:780px;text-align:center;font-size:14px;line-height:22px;color:var(--muted)}
.btn{position:absolute;display:flex;align-items:center;gap:14px;height:58px;padding:0 28px 0 6px;border-radius:29px;font-size:16px;font-weight:500;text-transform:uppercase;letter-spacing:.5px;white-space:nowrap}
.btn .dot{width:46px;height:46px;border-radius:50%;background:var(--white);display:flex;align-items:center;justify-content:center}
.btn-blue{background:var(--blue);color:var(--white)}
.btn-white{background:var(--white);color:var(--blue)}
.btn-white .dot{background:var(--orange)}
.placeholder{position:absolute}

/* header */
.site-header{top:0;height:104px;background:var(--white);box-shadow:0 2px 8px rgba(0,0,0,.06);z-index:5}
.brand{position:absolute;left:80px;top:26px;display:flex;align-items:center;gap:12px;font-size:44px;font-weight:700;color:var(--ink);line-height:52px}
.brand .mark{width:34px;height:34px;border-radius:50%;background:var(--orange)}
.main-nav{position:absolute;left:392px;top:42px;display:flex;gap:30px;font-size:15px;font-weight:500;color:var(--ink);text-transform:uppercase}
.main-nav .current{color:var(--orange)}
.search{position:absolute;left:1100px;top:40px}

/* hero */
.hero{top:104px;height:1090px}
.hero-photo{left:0;top:0;width:1200px;height:620px;background:linear-gradient(160deg,#6fa8c4 0%,#9ccbe0 35%,#d9c8a8 70%,#b89a74 100%)}
.hero-wave{position:absolute;left:0;top:520px}
.hero-kicker{position:absolute;left:76px;top:225px;font-size:36px;font-style:italic;color:var(--white)}
.hero-title{position:absolute;left:76px;top:270px;font-size:58px;font-weight:700;color:var(--white);letter-spacing:1px}
.slider-arrow{position:absolute;top:272px;width:46px;height:46px;border-radius:50%;background:rgba(40,45,50,.6);display:flex;align-items:center;justify-content:center}
.hero-device{left:780px;top:340px;width:400px;height:620px;border-radius:36px;background:linear-gradient(180deg,#3c4147 0%,#55606a 40%,#d8b49b 75%,#c99b7d 100%)}
.welcome-title{position:absolute;left:76px;top:650px;font-size:40px;font-style:italic;font-weight:500;color:var(--orange)}
.welcome-title b{font-weight:700}
.welcome-copy{position:absolute;left:76px;top:720px;width:680px;font-size:14px;line-height:23px;color:var(--text)}
.welcome-copy p+p{margin-top:14px}

/* how it works */
.how{top:1193px;height:467px;background:linear-gradient(180deg,#3b4045,#2f3438)}
.how .section-title{top:60px;color:var(--white)}
.how .section-lead{top:118px;color:#d2d6da}
.steps{position:absolute;left:0;top:210px;width:1200px;height:230px}
.step{position:absolute;top:0;width:150px;text-align:center}
.step .ring{width:138px;height:138px;margin:0 auto;border-radius:50%;background:var(--white);border:7px solid var(--orange);display:flex;align-items:center;justify-content:center;position:relative}
.step .num{position:absolute;left:-6px;top:-8px;width:32px;height:32px;border-radius:50%;background:var(--white);border:2px solid var(--orange);color:var(--orange);font-size:14px;font-weight:700;display:flex;align-items:center;justify-content:center}
.step .label{margin-top:26px;font-size:22px;color:var(--white)}
.chevron{position:absolute;top:50px}

/* benefits */
.benefits{top:1660px;height:900px;background:linear-gradient(180deg,#ffffff 0%,#eef5f8 40%,#e3eef3 100%)}
.benefits .section-title{top:55px}
.benefits .section-lead{top:112px}
.tab{position:absolute;top:200px;height:56px;border-radius:28px;display:flex;align-items:center;justify-content:center;font-size:16px;font-weight:500;text-transform:uppercase}
.tab-active{left:207px;width:388px;background:var(--blue);color:var(--white)}
.tab-idle{left:609px;width:378px;border:2px solid var(--blue);color:var(--blue)}
.benefit-device{left:170px;top:310px;width:340px;height:570px;border-radius:40px;background:linear-gradient(180deg,#8cc4dd 0%,#b9dbea 40%,#d8c6a6 80%,#b69a7c 100%)}
.play{position:absolute;left:280px;top:538px;width:90px;height:90px;border-radius:50%;background:rgba(30,34,38,.7);display:flex;align-items:center;justify-content:center}
.benefit{position:absolute;left:553px;width:560px;height:110px}
.benefit .icon{position:absolute;left:0;top:0;width:104px;height:104px;border-radius:50%;background:var(--white);border:5px solid var(--orange);display:flex;align-items:center;justify-content:center}
.benefit h3{position:absolute;left:150px;top:14px;font-size:28px;font-weight:400;color:var(--orange)}
.benefit p{position:absolute;left:150px;top:56px;width:360px;font-size:13px;line-height:20px;color:var(--text)}

/* who we are */
.who{top:2559px;height:398px;background:var(--blue)}
.who .section-title{top:50px;color:var(--white)}
.who .section-title .accent{color:var(--orange)}
.who-copy{position:absolute;left:150px;top:122px;width:900px;text-align:center;font-size:14px;line-height:22px;color:var(--white)}
.who-copy p+p{margin-top:8px}

/* articles */
.articles{top:2957px;height:622px;background:var(--white)}
.articles .section-title{top:50px}
.articles .section-lead{top:108px}
.card{position:absolute;top:190px;width:332px;height:365px;background:var(--white);box-shadow:0 2px 10px rgba(0,0,0,.08)}
.card .thumb{position:absolute;left:0;top:0;width:100%;height:165px}
.card h4{position:absolute;left:22px;top:190px;width:290px;font-size:24px;font-weight:400;line-height:30px;color:var(--ink)}
.card p{position:absolute;left:22px;top:258px;width:290px;font-size:14px;line-height:21px;color:var(--text)}
.card .more{position:absolute;left:22px;top:322px;font-size:14px;font-weight:500;color:var(--blue)}
.card-feature{background:var(--orange-soft)}
.card-feature .thumb{height:100%;background:linear-gradient(180deg,#f8a07a,#f47b4c)}
.card-feature h4,.card-feature p{color:var(--white)}
.card-feature h4{top:130px}
.card-feature p{top:198px}
.badge{position:absolute;left:-12px;top:-12px;width:52px;height:52px;border-radius:50%;background:var(--blue);border:4px solid var(--white);display:flex;align-items:center;justify-content:center}

/* faq */
.faq{top:3579px;height:605px;background:linear-gradient(120deg,#f8946a,#f27444)}
.faq-visual{left:0;top:0;width:590px;height:605px;background:linear-gradient(160deg,#6f8f5c 0%,#c9c6c0 35%,#e4e0da 70%,#d9d3ca 100%)}
.faq-title{position:absolute;left:800px;top:60px;font-size:42px;font-weight:500;color:var(--ink)}
.accordion{position:absolute;left:615px;top:130px;width:510px}
.q{height:58px;display:flex;align-items:center;justify-content:space-between;padding:0 18px;font-size:16px;color:var(--white);border-bottom:1px solid rgba(255,255,255,.35);background:rgba(255,255,255,.12)}
.q-open{background:var(--blue);border:none}
.answer{padding:18px;height:130px;font-size:14px;line-height:22px;color:var(--white);background:rgba(255,255,255,.2)}

/* contact */
.contact{top:4184px;height:605px;background:var(--white)}
.contact .section-title{top:35px}
.contact-lead{position:absolute;left:0;top:95px;width:100%;text-align:center;font-size:15px;font-style:italic;line-height:24px;color:var(--ink)}
.channel{position:absolute;top:185px;width:300px;text-align:center;font-size:15px;color:var(--ink);line-height:22px}
.channel .pin{width:72px;height:72px;margin:0 auto 18px;border-radius:50%;background:var(--orange);display:flex;align-items:center;justify-content:center}
.field{position:absolute;height:52px;border:1px solid var(--line);background:#f4f5f6;font-size:14px;font-style:italic;color:var(--muted);padding:16px 14px}
.field-active{border-color:var(--blue);background:var(--white);color:var(--orange)}

/* footer */
.site-footer{top:4789px;height:398px;background:linear-gradient(180deg,#2f3438,#22262a)}
.footer-brand{position:absolute;left:0;top:110px;width:100%;display:flex;justify-content:center;align-items:center;gap:14px;font-size:56px;font-weight:700;color:var(--white)}
.footer-brand .mark{width:40px;height:40px;border-radius:50%;background:var(--orange)}
.socials{position:absolute;left:0;top:205px;width:100%;display:flex;justify-content:center;gap:18px}
.socials span{width:46px;height:46px;border-radius:50%;background:var(--orange)}
.footer-nav{position:absolute;left:0;top:295px;width:100%;display:flex;justify-content:center;gap:28px;font-size:15px;color:var(--white)}
.copyright{position:absolute;left:0;top:330px;width:100%;text-align:center;font-size:13px;color:var(--orange)}
</style>
</head>
<body>

<header class="site-header">
  <div class="brand"><span class="mark"></span>zapply</div>
  <nav class="main-nav">
    <span class="current">Home ▾</span><span>How it works</span><span>Benefit</span><span>Who we are</span><span>Press</span><span>Get in touch</span><span>FAQ</span>
  </nav>
  <svg class="search" width="22" height="22" viewBox="0 0 22 22"><circle cx="9" cy="9" r="7" fill="none" stroke="#f26b3a" stroke-width="2.5"/><line x1="14" y1="14" x2="20" y2="20" stroke="#f26b3a" stroke-width="2.5"/></svg>
</header>

<section class="hero">
  <div class="placeholder hero-photo" role="img" aria-label="Couple relaxing in beach chairs with drinks by the sea"></div>
  <svg class="hero-wave" width="1200" height="110" viewBox="0 0 1200 110"><path d="M0 70 C300 10 700 130 1200 40 L1200 110 L0 110 Z" fill="#ffffff"/></svg>
  <div class="hero-kicker">Hospitality Zapply</div>
  <div class="hero-title">SIMPLE, FAST, EASY.</div>
  <div class="slider-arrow" style="left:16px"><svg width="14" height="18"><path d="M11 2 L3 9 L11 16" fill="none" stroke="#fff" stroke-width="3"/></svg></div>
  <div class="slider-arrow" style="left:1138px"><svg width="14" height="18"><path d="M3 2 L11 9 L3 16" fill="none" stroke="#fff" stroke-width="3"/></svg></div>
  <div class="placeholder hero-device" role="img" aria-label="Hand holding a smartphone showing the Zapply app welcome screen"></div>
  <h1 class="welcome-title">Welcome To <b>Zapply</b></h1>
  <div class="welcome-copy">
    <p>Lorem Ipsum is simply dummy text of the printing and typesetting industry. Lorem Ipsum has been the industry's standard dummy text ever since the 1500s, when an unknown printer took a galley of type and scrambled it to make a type specimen book.</p>
    <p>Lorem Ipsum is simply dummy text of the printing and typesetting industry. Lorem Ipsum has been the industry's standard dummy text ever since the 1500s, when an unknown printer took a galley of type and scrambled it to make a type specimen book. It has survived not only five centuries, but also the leap into electronic typesetting, remaining essentially unchanged. It was popularised in the 1960s with the release of Printset sheets.</p>
  </div>
  <div class="btn btn-blue" style="left:76px;top:958px"><span class="dot"><svg width="22" height="18"><path d="M2 9 H18 M12 3 L18 9 L12 15" fill="none" stroke="#f26b3a" stroke-width="3"/></svg></span>Learn more</div>
</section>

<section class="how">
  <h2 class="section-title"><span class="accent">How It</span> Works</h2>
  <p class="section-lead">Lorem Ipsum is simply dummy text of the printing and typesetting industry. Lorem Ipsum has been the industry's standard dummy text ever since the 1500s, when an unknown printer took a galley of type</p>
  <div class="steps">
    <div class="step" style="left:88px"><div class="ring"><span class="num">1</span><svg width="56" height="56" viewBox="0 0 56 56" fill="none" stroke="#f26b3a" stroke-width="3"><path d="M28 50 C16 36 12 28 12 21 a16 16 0 0 1 32 0 c0 7 -4 15 -16 29 Z"/><circle cx="28" cy="21" r="6"/></svg></div><div class="label">Locate</div></div>
    <div class="step" style="left:350px"><div class="ring"><span class="num">2</span><svg width="56" height="56" viewBox="0 0 56 56" fill="none" stroke="#f26b3a" stroke-width="3"><path d="M6 12 H24 Q28 12 28 16 V48 Q28 44 24 44 H6 Z M50 12 H32 Q28 12 28 16 V48 Q28 44 32 44 H50 Z"/></svg></div><div class="label">Browse</div></div>
    <div class="step" style="left:582px"><div class="ring"><span class="num">3</span><svg width="56" height="56" viewBox="0 0 56 56" fill="none" stroke="#f26b3a" stroke-width="3"><path d="M10 46 L46 10 M20 46 H46 V20"/></svg></div><div class="label">Order</div></div>
    <div class="step" style="left:814px"><div class="ring"><span class="num">4</span><svg width="56" height="56" viewBox="0 0 56 56" fill="none" stroke="#f26b3a" stroke-width="3"><rect x="8" y="26" width="10" height="20"/><path d="M18 28 L28 12 Q32 12 32 18 V24 H46 Q50 26 48 30 L44 44 Q42 46 38 46 H18"/></svg></div><div class="label">Help</div></div>
    <div class="step" style="left:1042px"><div class="ring"><span class="num">5</span><svg width="56" height="56" viewBox="0 0 56 56" fill="none" stroke="#f26b3a" stroke-width="3"><rect x="6" y="14" width="44" height="30" rx="4"/><line x1="6" y1="22" x2="50" y2="22"/><line x1="12" y1="36" x2="24" y2="36"/></svg></div><div class="label">Pay</div></div>
    <svg class="chevron" style="left:240px" width="110" height="40" viewBox="0 0 110 40"><line x1="0" y1="20" x2="110" y2="20" stroke="#f26b3a" stroke-width="6"/><path d="M42 4 L62 20 L42 36" fill="#f26b3a"/></svg>
    <svg class="chevron" style="left:500px" width="82" height="40" viewBox="0 0 82 40"><line x1="0" y1="20" x2="82" y2="20" stroke="#f26b3a" stroke-width="6"/><path d="M30 4 L50 20 L30 36" fill="#f26b3a"/></svg>
    <svg class="chevron" style="left:732px" width="82" height="40" viewBox="0 0 82 40"><line x1="0" y1="20" x2="82" y2="20" stroke="#f26b3a" stroke-width="6"/><path d="M30 4 L50 20 L30 36" fill="#f26b3a"/></svg>
    <svg class="chevron" style="left:964px" width="80" height="40" viewBox="0 0 80 40"><line x1="0" y1="20" x2="80" y2="20" stroke="#f26b3a" stroke-width="6"/><path d="M30 4 L50 20 L30 36" fill="#f26b3a"/></svg>
  </div>
</section>

<section class="benefits">
  <h2 class="section-title"><span class="accent">Our</span> Benifits</h2>
  <p class="section-lead">Lorem Ipsum is simply dummy text of the printing and typesetting industry. Lorem Ipsum has been the industry's standard dummy text ever since the 1500s, when an unknown printer took a galley of type</p>
  <div class="tab tab-active">The benefits for the guests</div>
  <div class="tab tab-idle">The benefits for the resort</div>
  <div class="placeholder benefit-device" role="img" aria-label="Hand holding a smartphone playing a video of guests on a beach"></div>
  <div class="play"><svg width="30" height="34"><path d="M4 2 L28 17 L4 32 Z" fill="#fff"/></svg></div>
  <div class="benefit" style="top:355px"><div class="icon"><svg width="48" height="48" viewBox="0 0 48 48" fill="none" stroke="#3a9bd5" stroke-width="3"><path d="M4 10 H20 Q24 10 24 14 V42 Q24 38 20 38 H4 Z M44 10 H28 Q24 10 24 14 V42 Q24 38 28 38 H44 Z"/></svg></div><h3>Menu</h3><p>See a visual for each item, and have all relevant dietary details provided to them – including allergens.</p></div>
  <div class="benefit" style="top:480px"><div class="icon"><svg width="48" height="48" viewBox="0 0 48 48" fill="none" stroke="#f26b3a" stroke-width="3"><rect x="14" y="4" width="20" height="40" rx="3"/><path d="M20 24 L23 27 L29 20"/></svg></div><h3>Customization</h3><p>customize the order and avoid human error.</p></div>
  <div class="benefit" style="top:612px"><div class="icon"><svg width="48" height="48" viewBox="0 0 48 48" fill="none" stroke="#f26b3a" stroke-width="3"><path d="M6 34 A18 18 0 1 1 42 34"/><line x1="24" y1="30" x2="33" y2="18"/><circle cx="24" cy="30" r="3"/></svg></div><h3>Speed</h3><p>No more time lost catching a waiter - Submit your orders/requests and lay back.</p></div>
  <div class="benefit" style="top:760px"><div class="icon"><svg width="48" height="48" viewBox="0 0 48 48" fill="none" stroke="#f26b3a" stroke-width="3"><rect x="4" y="12" width="40" height="26" rx="3"/><line x1="4" y1="20" x2="44" y2="20"/><line x1="10" y1="31" x2="22" y2="31"/></svg></div><h3>Fast Checkout</h3><p>Avoid waiting for the bill, use the saved credit card, or pay cash.</p></div>
</section>

<section class="who">
  <h2 class="section-title"><span class="accent">Who</span> We Are</h2>
  <div class="who-copy">
    <p>Lorem Ipsum is simply dummy text of the printing and typesetting industry. Lorem Ipsum has been the industry's standard dummy text ever since the 1500s, when an unknown printer took a galley of type and scrambled it to make a type specimen book.</p>
    <p>Lorem Ipsum is simply dummy text of the printing and typesetting industry. Lorem Ipsum has been the industry's standard dummy text ever since the 1500s, when an unknown printer took a galley of type and scrambled it to make a type specimen book. It has survived not only five centuries, but also the leap into electronic typesetting, remaining essentially unchanged.</p>
  </div>
  <div class="btn btn-white" style="left:490px;top:292px"><span class="dot"><svg width="22" height="18"><path d="M2 9 H18 M12 3 L18 9 L12 15" fill="none" stroke="#fff" stroke-width="3"/></svg></span>Learn more</div>
</section>

<section class="articles">
  <h2 class="section-title"><span class="accent">Latest</span> Articles</h2>
  <p class="section-lead">Lorem Ipsum is simply dummy text of the printing and typesetting industry. Lorem Ipsum has been the industry's standard dummy text ever since the 1500s, when an unknown printer took a galley of type</p>
  <article class="card card-feature" style="left:76px;overflow:visible">
    <div class="placeholder thumb" role="img" aria-label="Guest lounging with a tablet, tinted orange"></div>
    <span class="badge"><svg width="20" height="16"><path d="M2 8 H16 M11 3 L16 8 L11 13" fill="none" stroke="#fff" stroke-width="3"/></svg></span>
    <h4>Lorem Ipsum is simply dummy text.</h4>
    <p>Lorem Ipsum is simply dummy text of the printing and typesetting industry.</p>
    <div class="btn btn-blue" style="left:22px;top:288px;height:50px;font-size:14px"><span class="dot" style="width:40px;height:40px"><svg width="20" height="16"><path d="M2 8 H16 M11 3 L16 8 L11 13" fill="none" stroke="#f26b3a" stroke-width="3"/></svg></span>Read more</div>
  </article>
  <article class="card" style="left:432px">
    <div class="placeholder thumb" role="img" aria-label="Woman working on a laptop" style="background:linear-gradient(160deg,#e9e6e1,#c9bfb2)"></div>
    <h4>Lorem Ipsum is simply dummy text.</h4>
    <p>Lorem Ipsum is simply dummy text of the printing and typesetting industry.</p>
    <span class="more">READ MORE... »</span>
  </article>
  <article class="card" style="left:788px">
    <div class="placeholder thumb" role="img" aria-label="Couple playing on a sunny beach" style="background:linear-gradient(180deg,#5fa9d8 0%,#9fd0ea 50%,#e7d5b5 100%)"></div>
    <h4>Lorem Ipsum is simply dummy text.</h4>
    <p>Lorem Ipsum is simply dummy text of the printing and typesetting industry.</p>
    <span class="more">READ MORE... »</span>
  </article>
</section>

<section class="faq">
  <div class="placeholder faq-visual" role="img" aria-label="Hand holding a smartphone with the Zapply sign-up screen beside a potted plant"></div>
  <h2 class="faq-title">faq's</h2>
  <div class="accordion">
    <div class="q q-open"><span>Question 1</span><span style="font-size:28px">+</span></div>
    <div class="answer">Lorem Ipsum is simply dummy text of the printing and typesetting industry. Lorem Ipsum has been the industry's standard...</div>
    <div class="q"><span>Question 2</span><span>—</span></div>
    <div class="q"><span>Question 3</span><span>—</span></div>
    <div class="q"><span>Question 4</span><span>—</span></div>
    <div class="q"><span>Question 4</span><span>—</span></div>
  </div>
</section>

<section class="contact">
  <h2 class="section-title"><span class="accent">Get In</span> Touch</h2>
  <p class="contact-lead">Do You Want To Know More About Our Solutions, Or Try It For Free In Your Resort,<br>Contact Us :</p>
  <div class="channel" style="left:155px"><div class="pin"><svg width="30" height="36" viewBox="0 0 30 36"><path d="M15 34 C6 23 3 17 3 13 a12 12 0 0 1 24 0 c0 4 -3 10 -12 21 Z" fill="#fff"/><circle cx="15" cy="13" r="4.5" fill="#f26b3a"/></svg></div>Harbor Quarter - Coral Bay - Sunreef<br>Islands</div>
  <div class="channel" style="left:455px"><div class="pin"><svg width="32" height="32" viewBox="0 0 32 32"><path d="M8 3 L13 3 L15 10 L11 13 Q14 19 19 21 L22 17 L29 19 L29 24 Q28 29 23 29 Q5 27 3 9 Q3 4 8 3 Z" fill="#fff"/></svg></div>+971 5 23 47 90 12</div>
  <div class="channel" style="left:756px"><div class="pin"><svg width="34" height="26" viewBox="0 0 34 26"><rect x="1" y="1" width="32" height="24" rx="3" fill="#fff"/><path d="M2 3 L17 15 L32 3" fill="none" stroke="#f26b3a" stroke-width="2.5"/></svg></div>info@zapplyhub.example</div>
  <div class="field field-active" style="left:155px;top:330px;width:288px">Name*</div>
  <div class="field" style="left:460px;top:330px;width:284px">Email*</div>
  <div class="field" style="left:761px;top:330px;width:283px">Phone*</div>
  <div class="field" style="left:155px;top:398px;width:889px;height:90px">Message*</div>
  <div class="btn btn-blue" style="left:518px;top:500px"><span class="dot"><svg width="22" height="18"><path d="M2 9 H18 M12 3 L18 9 L12 15" fill="none" stroke="#f26b3a" stroke-width="3"/></svg></span>Submit</div>
</section>

<footer class="site-footer">
  <svg class="abs" style="left:0;top:0" width="1200" height="70" viewBox="0 0 1200 70"><path d="M0 0 H1200 V20 C800 70 400 -10 0 40 Z" fill="#ffffff"/><path d="M0 40 C400 -10 800 70 1200 20" fill="none" stroke="#f26b3a" stroke-width="6"/><path d="M0 48 C400 0 800 78 1200 28" fill="none" stroke="#3a9bd5" stroke-width="4"/></svg>
  <div class="footer-brand"><span class="mark"></span>zapply</div>
  <div class="socials"><span></span><span></span><span></span></div>
  <nav class="footer-nav"><span>Home</span><span>How it Works</span><span>Benefit</span><span>Who We Are</span><span>Press</span><span>Get in Touch</span><span>Faq</span></nav>
  <div class="copyright">Zapply - 2017 . All Rights Reserved.</div>
</footer>

</body>
</html>
```